Brightwell is a company offering Colon Hydrotherapy (or colonics)

Brightwell offers Colon Hydrotherapy using an innovative FDA approved system from the USA. The system is called the TORVA system. The clinic is based in Whangarei, Northland and is the first business of this kind for Northland.
I used to use a design from the Prontaleaf website - a water symbol. However, I want a design that will convey freshness. I want something new and clean which conveys vitality and revitalisation .... perhaps water or bubbles but which brings across the idea of detoxing (which is what colon hydrotherapy does)
The clinic will only be completed in April so for now I have put my mobile number but once in the clinic this will need to be changed to a landline number ... the email address will also change. Thanks for any ideas you give me,
Updates

Hi. I need the name Brightwell first and foremost as this is the name of the Company Underneath this it has to say Colon Hydrotherapy to let people know what Brightwell is My name underneath that would be Marian Holcombe And all contact details to follow this. Thanks !

Target Market(s)

People who are wanting to "detox" and focusing on their health and wellbeing

Industry/Entity Type

Clinic

Contact Information for Business Card

Brightwell
Colon Hydrotherapy
Marian Holcombe
Unit B, 42c Ferrand Lane, Whangarei

021 0487 3916
brightwellclinic@mailnest.example

Font styles to use
Serif

Colors
cee9f6
33a6d7
86cae6

Requirements
Must have
• Stand out with colour or logo

```html
<!DOCTYPE html>
<html lang="en">
<head>
<meta charset="utf-8">
<title>Brightwell – Business Card</title>
<link rel="stylesheet" href="https://fonts.googleapis.com/css2?family=Lora:ital,wght@0,400;0,600;1,400&display=swap">
<style>
  :root {
    --card-blue: #33a6d7;
    --wave-sky: #86cae6;
    --wave-mist: #cee9f6;
    --frame-mist: #cee9f6;
    --text-white: #ffffff;
    --text-deep: #15607f;
  }
  html, body {
    margin: 0;
    padding: 0;
    width: 1200px;
    height: 702px;
    overflow: hidden;
    background: #ffffff;
  }
  .card {
    position: relative;
    width: 1200px;
    height: 702px;
    background: var(--card-blue);
    overflow: hidden;
    font-family: "Lora", Georgia, serif;
    color: var(--text-white);
  }
  .card__art {
    position: absolute;
    inset: 0;
    width: 1200px;
    height: 702px;
  }
  .card__text {
    position: absolute;
    left: 78px;
    top: 130px;
    width: 620px;
  }
  .card__company {
    margin: 0;
    font-size: 74px;
    font-weight: 600;
    line-height: 1;
    letter-spacing: 0.5px;
  }
  .card__service {
    margin: 14px 0 0;
    font-size: 34px;
    font-style: italic;
    font-weight: 400;
    line-height: 1.2;
  }
  .card__person {
    margin: 34px 0 0;
    font-size: 30px;
    font-weight: 400;
    line-height: 1.2;
  }
  .card__contact {
    margin: 18px 0 0;
    padding: 0;
    list-style: none;
    font-size: 22px;
    line-height: 1.6;
  }
</style>
</head>
<body>
  <div class="card">
    <svg class="card__art" viewBox="0 0 1200 702" xmlns="http://www.w3.org/2000/svg">
      <defs>
        <linearGradient id="wave-fade" x1="0" y1="0" x2="1" y2="0">
          <stop offset="0" stop-color="#cee9f6"/>
          <stop offset="0.5" stop-color="#86cae6" stop-opacity="0.7"/>
          <stop offset="1" stop-color="#86cae6" stop-opacity="0.35"/>
        </linearGradient>
        <radialGradient id="cluster-tone" cx="0.62" cy="0.55" r="0.6">
          <stop offset="0" stop-color="#cee9f6" stop-opacity="0.8"/>
          <stop offset="0.7" stop-color="#cee9f6" stop-opacity="0.4"/>
          <stop offset="1" stop-color="#cee9f6" stop-opacity="0"/>
        </radialGradient>
      </defs>

      <path class="wave wave--upper" d="M0,503 C220,570 430,585 700,530 C900,490 1050,440 1200,432 L1200,702 L0,702 Z" fill="#86cae6" opacity="0.75"/>
      <path class="wave wave--lower" d="M0,585 C300,665 720,655 1200,500 L1200,702 L0,702 Z" fill="url(#wave-fade)"/>
      <path class="wave wave--base" d="M700,702 C900,690 1080,670 1200,655 L1200,702 Z" fill="#86cae6" opacity="0.8"/>

      <rect class="cluster" x="710" y="24" width="460" height="652" fill="url(#cluster-tone)" role="img" aria-label="Cluster of interlocking light gears"/>

      <rect class="frame" x="37" y="26" width="1126" height="644" fill="none" stroke="#cee9f6" stroke-width="7"/>
    </svg>

    <div class="card__text">
      <h1 class="card__company">Brightwell</h1>
      <p class="card__service">Colon Hydrotherapy</p>
      <p class="card__person">Marian Holcombe</p>
      <ul class="card__contact">
        <li>Unit B, 42c Ferrand Lane, Whangarei</li>
        <li>021 0487 3916</li>
        <li>brightwellclinic@mailnest.example</li>
      </ul>
    </div>
  </div>
</body>
</html>
```